Catalog copying current designs, web designs and copywrite.

I am looking for someone to recreate a draft catalog using the same design process.

My entire brief with the photo samples and icons would not fit in here. They are in the google docs folder as below:

https://files.brindlecove.net/share/folders/7qXk2mPz9LwRt4VhYs3NcB0aJdE6uFgHo?mode=viewer

```html
<!DOCTYPE html>
<html lang="en">
<head>
<meta charset="utf-8">
<title>Steadfast Crew – Labour Hire Catalogue</title>
<link href="https://fonts.googleapis.com/css2?family=Anton&family=Arimo:wght@400;700&family=Oswald:wght@500;700&display=swap" rel="stylesheet">
<style>
  :root{
    --red:#7a0d0d;
    --red-deep:#4a0707;
    --red-bright:#9b1010;
    --ink:#231f20;
    --slate:#2d3336;
    --grey:#8c9296;
    --paper:#f4f4f4;
    --paper-shade:#d9d9d9;
    --white:#ffffff;
  }
  *{margin:0;padding:0;box-sizing:border-box}
  html,body{width:1200px;height:528px;overflow:hidden;background:var(--white)}
  body{position:relative;font-family:"Arimo",Arial,sans-serif;color:var(--ink)}
  .panel{position:absolute;top:2px;width:366px;height:518px;overflow:hidden;
    background:linear-gradient(135deg,var(--paper) 0%,var(--white) 35%,var(--paper-shade) 55%,var(--white) 75%,var(--paper-shade) 100%)}
  .panel--cover{left:4px}
  .panel--about{left:408px;top:9px;height:518px}
  .panel--why{left:831px;top:9px;height:518px}
  .abs{position:absolute}
  .band{position:absolute;left:0;top:0;width:100%;height:100%}

  /* cover */
  .cover-photo{position:absolute;left:0;top:0;width:100%;height:100%;
    background:linear-gradient(160deg,#eceeef 0%,#dfe3e5 40%,#c8ccce 70%,#b9bcbd 100%)}
  .brand{position:absolute;left:30px;top:206px;display:flex;flex-direction:column;align-items:flex-start}
  .brand-row{display:flex;align-items:center;gap:6px}
  .brand-mark{width:9px;height:30px;background:var(--slate)}
  .brand-name{font-family:"Arimo",Arial,sans-serif;font-weight:700;font-size:26px;color:var(--red);line-height:1;letter-spacing:-.5px}
  .brand-tag{margin:3px 0 0 18px;font-size:5px;letter-spacing:3.6px;color:var(--slate);font-weight:700}

  /* vertical titles */
  .side-title{position:absolute;font-family:"Arimo",Arial,sans-serif;font-size:27px;color:var(--grey);letter-spacing:1px;
    transform:rotate(-90deg);transform-origin:left top;white-space:nowrap}

  /* about */
  .about-heading{left:28px;top:214px;font-family:"Anton",Impact,sans-serif;font-size:17px;line-height:19.5px;color:var(--ink);text-transform:uppercase}
  .about-heading .accent{color:var(--red)}
  .about-copy{left:28px;width:194px;font-size:7.3px;line-height:8.8px;text-align:justify;color:var(--ink)}
  .values{left:248px;top:267px;width:92px}
  .value{height:28px;border-radius:12px;background:var(--slate);border:3px solid var(--red);color:var(--white);
    font-family:"Anton",Impact,sans-serif;font-size:8.5px;display:flex;align-items:center;justify-content:center}
  .value-link{width:10px;height:21px;margin:0 auto;border-left:3px solid var(--red);border-right:3px solid var(--red)}
  .stats{left:28px;top:403px;width:196px;height:60px}
  .stats-line{position:absolute;left:20px;right:20px;top:18px;height:4px;background:var(--red)}
  .stat{position:absolute;top:0;width:50px;margin-left:-25px;text-align:center}
  .stat-num{width:42px;height:42px;margin:0 auto;border-radius:50%;background:var(--slate);border:3px solid var(--red);
    color:var(--white);font-family:"Anton",Impact,sans-serif;font-size:16px;display:flex;align-items:center;justify-content:center}
  .stat-label{margin-top:5px;font-family:"Anton",Impact,sans-serif;font-size:8px;line-height:9px;color:var(--red);text-transform:uppercase}

  /* why */
  .employer{left:146px;top:48px;width:70px;text-align:center}
  .employer-label{font-family:"Anton",Impact,sans-serif;font-size:14px;color:var(--ink);margin-top:2px}
  .step-num{font-family:"Anton",Impact,sans-serif;line-height:1;color:var(--red)}
  .step-title{font-family:"Oswald",sans-serif;font-weight:700;font-size:10px;letter-spacing:1.2px;color:var(--red)}
  .step-text{font-family:"Anton",Impact,sans-serif;font-size:9.2px;line-height:13.7px;color:var(--ink);text-align:justify}
  .step--light .step-num,.step--light .step-text{color:var(--white)}
  .step--light .step-title{color:var(--paper-shade)}
</style>
</head>
<body>

<section class="panel panel--cover">
  <div class="cover-photo" role="img" aria-label="Photo of a construction worker in a hard hat and hi-vis shirt looking up at a tower crane"></div>
  <svg class="band" viewBox="0 0 366 518" preserveAspectRatio="none" role="img" aria-label="Dark red faceted decorative band">
    <defs><linearGradient id="redA" x1="0" y1="0" x2="1" y2="1"><stop offset="0" stop-color="#5a0808"/><stop offset=".5" stop-color="#7a0d0d"/><stop offset="1" stop-color="#4a0707"/></linearGradient></defs>
    <polygon points="0,250 20,300 55,330 130,318 170,360 230,372 300,365 366,355 366,518 0,518" fill="url(#redA)"/>
  </svg>
  <div class="brand">
    <div class="brand-row"><span class="brand-mark"></span><span class="brand-name">steadfast crew</span></div>
    <div class="brand-tag">LABOUR HIRE SOLUTIONS</div>
  </div>
</section>

<section class="panel panel--about">
  <h2 class="side-title" style="left:24px;top:154px">ABOUT US</h2>
  <h1 class="abs about-heading">Industry leading recruitment &amp;<br><span class="accent">Labour hire agency<br>in New South Wales</span></h1>
  <p class="abs about-copy" style="top:279px">At Steadfast Crew, we're all about ensuring our clients achieve their goals and succeed in their field. This is why so many construction companies have trusted us in providing qualified workers for their projects. Make an enquiry and watch these words be put into action.</p>
  <p class="abs about-copy" style="top:340px">We are extremely passionate about what we do, excellence in the Labour Hire industry has become second nature for us. We work to give you many reasons to engage with Steadfast Crew services. We have become a well renowned Recruitment &amp; Labour Hire company by upholding the following values:</p>
  <div class="abs values">
    <div class="value">INSPIRING OTHERS</div>
    <div class="value-link"></div>
    <div class="value">ACHIEVING GOALS</div>
    <div class="value-link"></div>
    <div class="value">WORKING TO SUCCEED</div>
  </div>
  <div class="abs stats">
    <div class="stats-line"></div>
    <div class="stat" style="left:20px"><div class="stat-num">54</div><div class="stat-label">Satisfied<br>clients</div></div>
    <div class="stat" style="left:72px"><div class="stat-num">316</div><div class="stat-label">Employees</div></div>
    <div class="stat" style="left:124px"><div class="stat-num">8</div><div class="stat-label">Staff<br>members</div></div>
    <div class="stat" style="left:176px"><div class="stat-num">68</div><div class="stat-label">Jobsites</div></div>
  </div>
</section>

<section class="panel panel--why">
  <svg class="band" viewBox="0 0 366 518" preserveAspectRatio="none" role="img" aria-label="Dark red faceted decorative band">
    <defs><linearGradient id="redB" x1="0" y1="0" x2="1" y2="1"><stop offset="0" stop-color="#5a0808"/><stop offset=".5" stop-color="#7a0d0d"/><stop offset="1" stop-color="#4a0707"/></linearGradient></defs>
    <polygon points="0,245 25,300 45,320 110,325 170,360 240,375 300,365 360,358 366,518 0,518" fill="url(#redB)"/>
  </svg>
  <h2 class="side-title" style="left:30px;top:122px">WHY US</h2>
  <div class="abs employer">
    <svg width="58" height="58" viewBox="0 0 58 58" aria-hidden="true" fill="#7a0d0d">
      <circle cx="29" cy="5" r="4.5"/><rect x="23" y="11" width="12" height="10" rx="3"/>
      <path d="M5 26v-6h48v6" fill="none" stroke="#7a0d0d" stroke-width="3"/>
      <circle cx="12" cy="29" r="2"/><circle cx="22" cy="27" r="2"/><circle cx="36" cy="27" r="2"/><circle cx="46" cy="29" r="2"/>
      <g><circle cx="9" cy="36" r="4"/><rect x="4" y="41" width="10" height="16" rx="2"/></g>
      <g><circle cx="22" cy="36" r="4"/><rect x="17" y="41" width="10" height="16" rx="2"/></g>
      <g><circle cx="36" cy="36" r="4"/><rect x="31" y="41" width="10" height="16" rx="2"/></g>
      <g><circle cx="49" cy="36" r="4"/><rect x="44" y="41" width="10" height="16" rx="2"/></g>
    </svg>
    <div class="employer-label">EMPLOYER</div>
  </div>

  <div class="abs step-num" style="left:72px;top:140px;font-size:70px">1</div>
  <div class="abs step-title" style="left:112px;top:147px">INITIATION</div>
  <p class="abs step-text" style="left:112px;top:161px;width:195px">Steadfast Crew initially engages with the employer to create a buiness relationship. We understand the clients’ needs and assign appropriate measures to forward our services.</p>

  <div class="abs step-num" style="left:24px;top:232px;font-size:76px">2</div>
  <div class="abs step-title" style="left:71px;top:239px">ASSESSMENT</div>
  <p class="abs step-text" style="left:71px;top:253px;width:272px">We assess the employers’ criteria and hand over the appropriate candidates for their job. Unlike most recruitment companies, we do not bulk-send a bunch of resumes, but rather ensure that we are sending the greatest quality candidates that best meet their needs.</p>

  <div class="step step--light">
    <div class="abs step-num" style="left:62px;top:392px;font-size:76px">3</div>
    <div class="abs step-title" style="left:112px;top:400px">PLACEMENT</div>
    <p class="abs step-text" style="left:112px;top:414px;width:183px">Employers then interview the candidate put forward by Steadfast Crew in order to fill the vacancy and ensure that the candidate is the best fit for their position.</p>
  </div>
</section>

</body>
</html>
```